I would like a business card to match my truck wrap and logo. I would like the font to match my existing business card please.

Industry/Entity Type

Painter

Contact Information for Business Card

Rodrigo Venaza 801-437-2916 Venazacoatings.utah@brushmail.net
SERVICES - Custom Paint & Stain, Interior & Exterior, Epoxy Coatings / Garage Floors, Cabinet Refinishing, Log Staining and Refinishing.

Requirements
Nice to have
• I would like to have the white and grey line like the bottom of my vehicle wrap, Light Grey to match my truck also.

```html
<!DOCTYPE html>
<html lang="en">
<head>
<meta charset="utf-8">
<title>Venaza Painting – Business Card</title>
<link href="https://fonts.googleapis.com/css2?family=Arimo:wght@400;700&display=swap" rel="stylesheet">
<style>
  :root {
    --backdrop: #2a2d32;
    --card: #ffffff;
    --brand-blue: #1a8ad4;
    --name-blue: #1677c4;
    --text-grey: #6b6e72;
    --trim-grey: #d9dbde;
    --divider: #55585c;
  }
  * { box-sizing: border-box; margin: 0; padding: 0; }
  html, body {
    width: 1200px; height: 900px; overflow: hidden;
    background: var(--backdrop);
    font-family: "Arimo", Arial, sans-serif;
  }
  .sheet {
    position: relative; width: 1200px; height: 900px;
    display: flex; flex-direction: column; align-items: center; justify-content: center; gap: 60px;
  }
  .card {
    position: relative; width: 560px; height: 320px;
    background: var(--card);
    box-shadow: 0 10px 28px rgba(0,0,0,.45);
    overflow: hidden;
  }
  /* Front */
  .card-front .trim-band {
    position: absolute; left: 0; right: 0; top: 244px; height: 36px;
    background: linear-gradient(180deg, #ffffff 0%, var(--trim-grey) 50%, #ffffff 100%);
  }
  .card-front .brand {
    position: absolute; left: 46px; top: 92px; width: 200px;
    display: flex; align-items: center; gap: 12px;
  }
  .brand-square { width: 30px; height: 30px; background: var(--brand-blue); flex: none; }
  .brand-name {
    color: var(--brand-blue); font-weight: 700; font-size: 25px; line-height: 1.05;
    letter-spacing: .5px; text-transform: uppercase;
  }
  .card-front .divider {
    position: absolute; left: 262px; top: 78px; width: 1.5px; height: 78px; background: var(--divider);
  }
  .contact { position: absolute; left: 282px; top: 82px; }
  .contact .person {
    color: var(--name-blue); font-size: 21px; font-weight: 400; text-transform: uppercase;
    letter-spacing: .3px; margin-bottom: 9px;
  }
  .contact .line { color: var(--text-grey); font-size: 15px; line-height: 1.45; }
  /* Back */
  .card-back .brand-square {
    position: absolute; left: 50%; top: 84px; width: 36px; height: 36px; margin-left: -18px;
  }
  .services {
    position: absolute; left: 40px; right: 40px; top: 150px;
    color: var(--text-grey); font-size: 13.5px; line-height: 1.55;
  }
</style>
</head>
<body>
<main class="sheet">
  <section class="card card-front" aria-label="Business card front">
    <div class="trim-band" role="img" aria-label="Light grey trim lines matching the truck wrap"></div>
    <div class="brand">
      <span class="brand-square"></span>
      <span class="brand-name">Venaza<br>Painting</span>
    </div>
    <div class="divider"></div>
    <div class="contact">
      <p class="person">Rodrigo Venaza</p>
      <p class="line">801-437-2916</p>
      <p class="line">Venazacoatings.utah@brushmail.net</p>
    </div>
  </section>

  <section class="card card-back" aria-label="Business card back">
    <span class="brand-square"></span>
    <p class="services">SERVICES - Custom Paint &amp; Stain, Interior &amp; Exterior, Epoxy Coatings / Garage Floors, Cabinet Refinishing, Log Staining and Refinishing.</p>
  </section>
</main>
</body>
</html>
```